standardize print collateral

we need help standardizing all print collateral and website. top priorities:

1. standardized case studies template
2. standardized marketing slicks template
3. standardized powerpoint template
Updates

Project Deadline Extended
Reason: We are extending the project to allow current design submissions to be tweaked while providing the opportunity for new designs to be submitted. We will need all 3 collateral designs submitted to make a final decision. Please note, these 3 designs should all look different, needless to say they should all compliment eachother. As for some direction, the powerpoint main color should not be yellow since yellow does not show up the same shade on any screen. The case study and marketing slicks will be printed and often sit next to our competitors marketing material - think high end product, technology, revolutionary, edgy, professional. The designs should compliment eachother and feel like the Brightfen Metrics brand (which you are determining) and should stand out professionally. We are open to introducing new colors into our brand, the only thing that must remain the same is our logo. Have fun, make it edgy, and keep it professional. Looking forward to seeing what you submit!

Target Market(s)

Property Casualty Insurance Companies: Executive level wording with actuarial credibility

Industry/Entity Type

Marketing

Requirements
Must have
• professional layout for existing collateral and 2-page marketing slicks. style guide/colors can be transferred to powerpoint. logo must stay; everything else (i.e. color, font, layout/structure etc.) is flexible. The three components should not looks the same, they should only compliment eachother.
Nice to have
• we are revolutionizing a conservative industry, so adequate level of edgy/advanced technology/impactful feel to layout
Should not have
• no need to stay within color constraints of yellow, but need to appropriately work well with the eagle head logo

```html
<!DOCTYPE html>
<html lang="en">
<head>
<meta charset="utf-8">
<title>Rapid Portfolio Analysis – Marketing Slick Options</title>
<link rel="stylesheet" href="https://fonts.googleapis.com/css2?family=Barlow:wght@400;500;600;700&family=Barlow+Semi+Condensed:wght@500;600;700&family=Arimo:wght@700&display=swap">
<style>
  :root {
    --backdrop: #e8e3da;
    --paper: #ffffff;
    --brand-blue: #1f7dc0;
    --brand-blue-deep: #155f9c;
    --brand-blue-light: #8dd0f2;
    --teal-panel: #5ba7be;
    --teal-soft: #cfe6ee;
    --ink: #222a33;
    --ink-soft: #4a5562;
    --label-ink: #151515;
    --rule: #7fb4d6;
  }
  * { box-sizing: border-box; margin: 0; padding: 0; }
  html, body { width: 1200px; height: 1085px; overflow: hidden; }
  body {
    position: relative;
    background: var(--backdrop);
    font-family: "Barlow", Arial, sans-serif;
    color: var(--ink);
  }

  .option-label {
    position: absolute;
    font-family: "Arimo", Arial, sans-serif;
    font-weight: 700;
    font-size: 21px;
    color: var(--label-ink);
  }

  .sheet {
    position: absolute;
    width: 375px;
    height: 485px;
    background: var(--paper);
    overflow: hidden;
    box-shadow: 0 2px 6px rgba(0,0,0,.25);
  }

  /* ---------- front header ---------- */
  .sheet-head {
    position: absolute; left: 0; top: 0; width: 100%; height: 78px;
    background: linear-gradient(180deg, #2a8fd2 0%, var(--brand-blue) 60%, #1c74b4 100%);
  }
  .sheet-title {
    position: absolute; left: 22px; top: 12px;
    font-family: "Barlow", Arial, sans-serif;
    font-weight: 500; font-size: 19px; line-height: 18px;
    color: #fff; text-transform: uppercase; letter-spacing: .3px;
  }
  .sheet-title .accent { color: var(--brand-blue-light); display: block; }
  .sheet-tagline {
    position: absolute; left: 22px; top: 52px;
    font-family: "Barlow Semi Condensed", Arial, sans-serif;
    font-size: 8.5px; font-weight: 500; color: #e6f3fb; letter-spacing: .2px;
  }
  .sheet-tagline strong { color: #fff; font-weight: 700; }

  .hero-art {
    position: absolute; left: 0; top: 78px; width: 250px; height: 178px;
  }
  .art-rising-bars { background: linear-gradient(135deg, #ffffff 0%, #e9eef3 45%, #c9a45a 78%, #2f78c4 100%); }
  .art-arrow-blocks { background: linear-gradient(160deg, #0e3e7a 0%, #2f79c4 45%, #b6d8f0 80%, #e9f3fb 100%); }
  .art-hand-chart { background: linear-gradient(160deg, #f4f6f8 0%, #dfe7ee 45%, #5f95c9 75%, #2b2f36 100%); }
  .art-puzzle-hands { background: linear-gradient(150deg, #f3f5f7 0%, #dfe4e9 40%, #3d7fc2 70%, #e7c8b0 100%); }

  .intro-panel {
    position: absolute; right: 0; top: 76px; width: 150px; height: 183px;
  }
  .intro-panel svg { position: absolute; inset: 0; }
  .intro-panel p {
    position: absolute; left: 12px; right: 6px; top: 6px;
    font-size: 7.1px; line-height: 8.35px; font-weight: 600;
    color: #fff; text-align: center;
  }

  .how-tab {
    position: absolute; left: 0; top: 255px; width: 152px; height: 16px;
    background: var(--brand-blue);
    color: #fff; font-family: "Barlow Semi Condensed", Arial, sans-serif;
    font-size: 11px; font-weight: 500; line-height: 16px; padding-left: 20px;
  }
  .how-rule { position: absolute; left: 0; right: 0; top: 270px; height: 1px; background: var(--rule); }

  .steps {
    position: absolute; left: 22px; right: 12px; top: 282px; height: 100px;
    display: grid; grid-template-columns: repeat(3, 1fr); column-gap: 8px;
  }
  .step { border-right: 1px dotted var(--rule); padding-right: 6px; }
  .step:last-child { border-right: none; }
  .step-kicker {
    font-family: "Barlow Semi Condensed", Arial, sans-serif;
    font-size: 7.6px; font-weight: 700; color: var(--brand-blue); line-height: 8px;
  }
  .step-question {
    font-family: "Barlow Semi Condensed", Arial, sans-serif;
    font-size: 7.6px; font-weight: 700; color: var(--ink); line-height: 8px; margin-bottom: 5px;
  }
  .step p { font-size: 6.1px; line-height: 7.1px; color: var(--ink-soft); }

  .report-box {
    position: absolute; left: 20px; right: 18px; top: 390px; height: 63px;
    background: var(--brand-blue); padding: 5px 9px;
  }
  .report-box h3 {
    font-family: "Barlow Semi Condensed", Arial, sans-serif;
    font-size: 7.6px; font-weight: 700; color: var(--brand-blue-light); margin-bottom: 5px; letter-spacing: .2px;
  }
  .report-box p { font-size: 6.1px; line-height: 7.3px; color: #eaf4fb; }

  /* option 4 variations */
  .sheet-tall { height: 489px; }
  .sheet-tall .sheet-title { font-size: 23px; line-height: 22px; top: 18px; }
  .sheet-tall .hero-art { top: 78px; height: 180px; }
  .sheet-tall .intro-panel { top: 78px; }
  .sheet-tall .how-tab { top: 256px; }
  .sheet-tall .how-rule { top: 271px; }
  .sheet-tall .steps { top: 284px; }
  .sheet-tall .report-box { top: 392px; height: 66px; }

  /* ---------- back page ---------- */
  .back-band { position: absolute; left: 0; top: 0; width: 100%; height: 36px; }
  .back-grid {
    position: absolute; left: 20px; right: 20px;
    display: grid; grid-template-columns: 1fr 1fr; column-gap: 14px;
  }
  .back-kicker {
    font-family: "Barlow Semi Condensed", Arial, sans-serif;
    font-size: 6.6px; font-weight: 700; color: var(--brand-blue); margin-bottom: 3px;
  }
  .back-caption { font-size: 5.4px; line-height: 6.4px; color: var(--ink-soft); margin-top: 3px; }
  .back-statement {
    position: absolute; left: 22px; right: 22px; top: 144px;
    font-size: 8.4px; line-height: 10.2px; font-weight: 600; color: #1d4f7e;
  }
  .section-bar {
    position: absolute; left: 0; right: 0; height: 13px;
    background: var(--teal-soft);
  }
  .section-bar span {
    position: absolute; top: 0; line-height: 13px;
    font-family: "Barlow Semi Condensed", Arial, sans-serif;
    font-size: 6.6px; font-weight: 700; color: var(--brand-blue);
  }
  .back-note {
    position: absolute; left: 40px; right: 40px; top: 321px;
    font-size: 6.2px; line-height: 7.4px; color: var(--ink-soft);
  }
  .back-footer {
    position: absolute; left: 0; right: 0; bottom: 0; height: 54px;
    background: linear-gradient(180deg, #d7e9ef, #c3dee7);
  }
  .footer-about {
    position: absolute; left: 22px; top: 12px; width: 92px;
    font-size: 4.6px; line-height: 5.6px; color: var(--ink-soft);
  }
  .footer-brand {
    position: absolute; left: 128px; top: 19px; display: flex; align-items: center; gap: 4px;
    font-size: 8px; font-weight: 700; color: #1d4f7e;
  }
  .footer-brand i { display: block; width: 7px; height: 7px; border-radius: 50%; background: var(--brand-blue); }
  .footer-contact {
    position: absolute; right: 22px; top: 12px; width: 120px; text-align: right;
    font-size: 4.8px; line-height: 6px; color: var(--ink-soft);
  }
  .footer-contact strong { color: #1d4f7e; font-weight: 600; letter-spacing: .4px; }
</style>
</head>
<body>

  <!-- ===== Option 1 ===== -->
  <div class="option-label" style="left:24px; top:10px;">Front 1</div>
  <section class="sheet" style="left:18px; top:59px;">
    <header class="sheet-head">
      <h1 class="sheet-title">Rapid Portfolio<span class="accent">Analysis</span></h1>
      <p class="sheet-tagline">WINNING AGAINST <strong>ADVERSE SELECTION</strong></p>
    </header>
    <div class="hero-art art-rising-bars" role="img" aria-label="Rising blue arrow over golden 3D bar chart"></div>
    <div class="intro-panel">
      <svg width="150" height="183" viewBox="0 0 150 183" preserveAspectRatio="none"><polygon points="0,0 150,0 150,183 34,183" fill="#5ba7be"/></svg>
      <p>The property and casualty market is over-supplied with excess capacity, and current pricing methods are inconsistent and outdated. This leads to a considerable level of adverse selection within nearly every portfolio. Almost every insurer is attracting customers who are underpriced and losing business where they are overpriced. This invisible effect only surfaces after evidence of slowly deteriorating portfolio loss ratios, resulting in premium increases across the portfolio. These across-the-board premium increases exacerbate the problem by overpricing the most profitable customers and driving them into the arms of competitors.</p>
    </div>
    <div class="how-tab">HOW DOES IT WORK?</div>
    <div class="how-rule"></div>
    <div class="steps">
      <div class="step"><div class="step-kicker">DETECTION</div><div class="step-question">Is the portfolio priced correctly?</div><p>Veltrisk employs a regression method based on a technological breakthrough. It exposes pricing imbalances by commonly employed rating method including the GLM. These pricing imbalances are the major drivers of adverse selection.</p></div>
      <div class="step"><div class="step-kicker">MEASUREMENT</div><div class="step-question">How is the portfolio trending?</div><p>Veltrisk scores the two most important attributes of the portfolio: the adequacy of rates and the quality of the business on a progressive basis. In addition, Veltrisk projects the financial outcome of business as it is written with starting accuracy. Insurers are able to know significantly in advance of trends in their business.</p></div>
      <div class="step"><div class="step-kicker">CORRECTION</div><div class="step-question">How to address the issues?</div><p>Veltrisk provides an array of options for addressing any deterioration in the portfolio. These options range from specifically designed rate adjustments and underwriting strategies, to simple distribution management sales and profitability strategies.</p></div>
    </div>
    <div class="report-box">
      <h3>LET BRIGHTFEN METRICS BUILD YOUR PORTFOLIO ANALYSIS REPORT</h3>
      <p>The report details your portfolio trends and identifies future unseen problems before they occur. The insight provided in the report exhibits what is actually going on in your portfolio. This likely includes adverse selection, impact of price changes with unintended consequences, and the emerging trends in the composition of the book. The analysis results not only reveal past trends, but also predict future impact.</p>
    </div>
  </section>

  <!-- ===== Option 2 ===== -->
  <div class="option-label" style="left:412px; top:10px;">Front 2</div>
  <section class="sheet" style="left:412px; top:59px;">
    <header class="sheet-head">
      <h1 class="sheet-title">Rapid Portfolio<span class="accent">Analysis</span></h1>
      <p class="sheet-tagline">WINNING AGAINST <strong>ADVERSE SELECTION</strong></p>
    </header>
    <div class="hero-art art-arrow-blocks" role="img" aria-label="Deep blue 3D bars with a white arrow rising through them"></div>
    <div class="intro-panel">
      <svg width="150" height="183" viewBox="0 0 150 183" preserveAspectRatio="none"><polygon points="0,0 150,0 150,183 34,183" fill="#5ba7be"/></svg>
      <p>The property and casualty market is over-supplied with excess capacity, and current pricing methods are inconsistent and outdated. This leads to a considerable level of adverse selection within nearly every portfolio. Almost every insurer is attracting customers who are underpriced and losing business where they are overpriced. This invisible effect only surfaces after evidence of slowly deteriorating portfolio loss ratios, resulting in premium increases across the portfolio. These across-the-board premium increases exacerbate the problem by overpricing the most profitable customers and driving them into the arms of competitors.</p>
    </div>
    <div class="how-tab">HOW DOES IT WORK?</div>
    <div class="how-rule"></div>
    <div class="steps">
      <div class="step"><div class="step-kicker">DETECTION</div><div class="step-question">Is the portfolio priced correctly?</div><p>Veltrisk employs a regression method based on a technological breakthrough. It exposes pricing imbalances by commonly employed rating method including the GLM. These pricing imbalances are the major drivers of adverse selection.</p></div>
      <div class="step"><div class="step-kicker">MEASUREMENT</div><div class="step-question">How is the portfolio trending?</div><p>Veltrisk scores the two most important attributes of the portfolio: the adequacy of rates and the quality of the business on a progressive basis. In addition, Veltrisk projects the financial outcome of business as it is written with starting accuracy. Insurers are able to know significantly in advance of trends in their business.</p></div>
      <div class="step"><div class="step-kicker">CORRECTION</div><div class="step-question">How to address the issues?</div><p>Veltrisk provides an array of options for addressing any deterioration in the portfolio. These options range from specifically designed rate adjustments and underwriting strategies, to simple distribution management sales and profitability strategies.</p></div>
    </div>
    <div class="report-box">
      <h3>LET BRIGHTFEN METRICS BUILD YOUR PORTFOLIO ANALYSIS REPORT</h3>
      <p>The report details your portfolio trends and identifies future unseen problems before they occur. The insight provided in the report exhibits what is actually going on in your portfolio. This likely includes adverse selection, impact of price changes with unintended consequences, and the emerging trends in the composition of the book. The analysis results not only reveal past trends, but also predict future impact.</p>
    </div>
  </section>

  <!-- ===== Option 3 ===== -->
  <div class="option-label" style="left:805px; top:10px;">Front 3</div>
  <section class="sheet" style="left:805px; top:59px;">
    <header class="sheet-head">
      <h1 class="sheet-title">Rapid Portfolio<span class="accent">Analysis</span></h1>
      <p class="sheet-tagline">WINNING AGAINST <strong>ADVERSE SELECTION</strong></p>
    </header>
    <div class="hero-art art-hand-chart" role="img" aria-label="Hand holding a small blue bar chart against a light grid"></div>
    <div class="intro-panel">
      <svg width="150" height="183" viewBox="0 0 150 183" preserveAspectRatio="none"><polygon points="0,0 150,0 150,183 34,183" fill="#5ba7be"/></svg>
      <p>The property and casualty market is over-supplied with excess capacity, and current pricing methods are inconsistent and outdated. This leads to a considerable level of adverse selection within nearly every portfolio. Almost every insurer is attracting customers who are underpriced and losing business where they are overpriced. This invisible effect only surfaces after evidence of slowly deteriorating portfolio loss ratios, resulting in premium increases across the portfolio. These across-the-board premium increases exacerbate the problem by overpricing the most profitable customers and driving them into the arms of competitors.</p>
    </div>
    <div class="how-tab">HOW DOES IT WORK?</div>
    <div class="how-rule"></div>
    <div class="steps">
      <div class="step"><div class="step-kicker">DETECTION</div><div class="step-question">Is the portfolio priced correctly?</div><p>Veltrisk employs a regression method based on a technological breakthrough. It exposes pricing imbalances by commonly employed rating method including the GLM. These pricing imbalances are the major drivers of adverse selection.</p></div>
      <div class="step"><div class="step-kicker">MEASUREMENT</div><div class="step-question">How is the portfolio trending?</div><p>Veltrisk scores the two most important attributes of the portfolio: the adequacy of rates and the quality of the business on a progressive basis. In addition, Veltrisk projects the financial outcome of business as it is written with starting accuracy. Insurers are able to know significantly in advance of trends in their business.</p></div>
      <div class="step"><div class="step-kicker">CORRECTION</div><div class="step-question">How to address the issues?</div><p>Veltrisk provides an array of options for addressing any deterioration in the portfolio. These options range from specifically designed rate adjustments and underwriting strategies, to simple distribution management sales and profitability strategies.</p></div>
    </div>
    <div class="report-box">
      <h3>LET BRIGHTFEN METRICS BUILD YOUR PORTFOLIO ANALYSIS REPORT</h3>
      <p>The report details your portfolio trends and identifies future unseen problems before they occur. The insight provided in the report exhibits what is actually going on in your portfolio. This likely includes adverse selection, impact of price changes with unintended consequences, and the emerging trends in the composition of the book. The analysis results not only reveal past trends, but also predict future impact.</p>
    </div>
  </section>

  <!-- ===== Option 4 ===== -->
  <div class="option-label" style="left:24px; top:553px;">Front 4</div>
  <section class="sheet sheet-tall" style="left:18px; top:580px;">
    <header class="sheet-head">
      <h1 class="sheet-title">Rapid Portfolio<span class="accent">Analysis</span></h1>
    </header>
    <div class="hero-art art-puzzle-hands" role="img" aria-label="Hands joining four blue puzzle pieces reading Winning, Against, Adverse, Selection"></div>
    <div class="intro-panel">
      <svg width="150" height="183" viewBox="0 0 150 183" preserveAspectRatio="none"><polygon points="0,0 150,0 150,183 34,183" fill="#5ba7be"/></svg>
      <p>The property and casualty market is over-supplied with excess capacity, and current pricing methods are inconsistent and outdated. This leads to a considerable level of adverse selection within nearly every portfolio. Almost every insurer is attracting customers who are underpriced and losing business where they are overpriced. This invisible effect only surfaces after evidence of slowly deteriorating portfolio loss ratios, resulting in premium increases across the portfolio. These across-the-board premium increases exacerbate the problem by overpricing the most profitable customers and driving them into the arms of competitors.</p>
    </div>
    <div class="how-tab">HOW DOES IT WORK?</div>
    <div class="how-rule"></div>
    <div class="steps">
      <div class="step"><div class="step-kicker">DETECTION</div><div class="step-question">Is the portfolio priced correctly?</div><p>Veltrisk employs a regression method based on a technological breakthrough. It exposes pricing imbalances by commonly employed rating method including the GLM. These pricing imbalances are the major drivers of adverse selection.</p></div>
      <div class="step"><div class="step-kicker">MEASUREMENT</div><div class="step-question">How is the portfolio trending?</div><p>Veltrisk scores the two most important attributes of the portfolio: the adequacy of rates and the quality of the business on a progressive basis. In addition, Veltrisk projects the financial outcome of business as it is written with starting accuracy. Insurers are able to know significantly in advance of trends in their business.</p></div>
      <div class="step"><div class="step-kicker">CORRECTION</div><div class="step-question">How to address the issues?</div><p>Veltrisk provides an array of options for addressing any deterioration in the portfolio. These options range from specifically designed rate adjustments and underwriting strategies, to simple distribution management sales and profitability strategies.</p></div>
    </div>
    <div class="report-box">
      <h3>LET BRIGHTFEN METRICS BUILD YOUR PORTFOLIO ANALYSIS REPORT</h3>
      <p>The report details your portfolio trends and identifies future unseen problems before they occur. The insight provided in the report exhibits what is actually going on in your portfolio. This likely includes adverse selection, impact of price changes with unintended consequences, and the emerging trends in the composition of the book. The analysis results not only reveal past trends, but also predict future impact.</p>
    </div>
  </section>

  <!-- ===== Back page ===== -->
  <div class="option-label" style="left:412px; top:553px;">Back</div>
  <section class="sheet" style="left:412px; top:580px; height:487px;">
    <svg class="back-band" viewBox="0 0 375 36" preserveAspectRatio="none" aria-hidden="true">
      <path d="M0,14 C120,4 250,2 375,6 L375,36 L0,36 Z" fill="#1f7dc0"/>
      <path d="M0,14 C120,4 250,2 375,6 L375,11 C250,8 120,10 0,20 Z" fill="#8dd0f2"/>
    </svg>

    <div class="back-grid" style="top:40px;">
      <div>
        <div class="back-kicker">PORTFOLIO MONITORING</div>
        <svg width="160" height="64" viewBox="0 0 160 64" aria-label="Portfolio monitoring table">
          <rect x="0" y="0" width="160" height="8" fill="#dfe7ef"/>
          <g stroke="#c9d3dc" stroke-width=".5">
            <line x1="0" y1="8" x2="160" y2="8"/><line x1="0" y1="16" x2="160" y2="16"/><line x1="0" y1="24" x2="160" y2="24"/><line x1="0" y1="32" x2="160" y2="32"/><line x1="0" y1="40" x2="160" y2="40"/><line x1="0" y1="48" x2="160" y2="48"/><line x1="0" y1="56" x2="160" y2="56"/><line x1="0" y1="64" x2="160" y2="64"/>
            <line x1="28" y1="0" x2="28" y2="64"/><line x1="54" y1="0" x2="54" y2="64"/><line x1="80" y1="0" x2="80" y2="64"/><line x1="104" y1="0" x2="104" y2="64"/><line x1="122" y1="0" x2="122" y2="64"/><line x1="141" y1="0" x2="141" y2="64"/>
          </g>
          <g fill="#cf3a3a"><rect x="104.5" y="8.5" width="17" height="7"/><rect x="104.5" y="24.5" width="17" height="7"/></g>
          <g fill="#f2c14b"><rect x="104.5" y="16.5" width="17" height="7"/><rect x="122.5" y="32.5" width="18" height="7"/></g>
          <g fill="#7dc36b"><rect x="104.5" y="40.5" width="17" height="7"/><rect x="104.5" y="48.5" width="17" height="7"/><rect x="122.5" y="48.5" width="18" height="7"/></g>
          <g fill="#8a95a0"><rect x="4" y="11" width="18" height="2"/><rect x="4" y="19" width="18" height="2"/><rect x="4" y="27" width="18" height="2"/><rect x="4" y="35" width="18" height="2"/><rect x="4" y="43" width="18" height="2"/><rect x="4" y="51" width="18" height="2"/><rect x="4" y="59" width="18" height="2"/>
            <rect x="32" y="11" width="16" height="2"/><rect x="32" y="19" width="16" height="2"/><rect x="32" y="27" width="16" height="2"/><rect x="32" y="35" width="16" height="2"/><rect x="32" y="43" width="16" height="2"/><rect x="32" y="51" width="16" height="2"/><rect x="32" y="59" width="16" height="2"/>
            <rect x="58" y="11" width="16" height="2"/><rect x="58" y="19" width="16" height="2"/><rect x="58" y="27" width="16" height="2"/><rect x="58" y="35" width="16" height="2"/><rect x="58" y="43" width="16" height="2"/><rect x="58" y="51" width="16" height="2"/><rect x="58" y="59" width="16" height="2"/></g>
        </svg>
        <p class="back-caption">Predict the future loss ratio of the business being written – both renewals and new business.</p>
      </div>
      <div>
        <div class="back-kicker">DISTRIBUTION MONITORING</div>
        <svg width="160" height="64" viewBox="0 0 160 64" aria-label="Distribution heat map table">
          <rect x="0" y="0" width="160" height="64" fill="#f4f6f8" stroke="#c9d3dc" stroke-width=".5"/>
          <g>
            <rect x="0" y="0" width="160" height="6" fill="#dfe7ef"/>
            <rect x="30" y="8" width="26" height="7" fill="#7dc36b"/><rect x="56" y="8" width="26" height="7" fill="#f2c14b"/><rect x="82" y="8" width="26" height="7" fill="#cf3a3a"/><rect x="108" y="8" width="26" height="7" fill="#7dc36b"/><rect x="134" y="8" width="26" height="7" fill="#f2c14b"/>
            <rect x="30" y="16" width="26" height="7" fill="#f2c14b"/><rect x="56" y="16" width="26" height="7" fill="#cf3a3a"/><rect x="82" y="16" width="26" height="7" fill="#7dc36b"/><rect x="108" y="16" width="26" height="7" fill="#7dc36b"/><rect x="134" y="16" width="26" height="7" fill="#cf3a3a"/>
            <rect x="30" y="24" width="26" height="7" fill="#7dc36b"/><rect x="56" y="24" width="26" height="7" fill="#7dc36b"/><rect x="82" y="24" width="26" height="7" fill="#f2c14b"/><rect x="108" y="24" width="26" height="7" fill="#cf3a3a"/><rect x="134" y="24" width="26" height="7" fill="#7dc36b"/>
            <rect x="30" y="32" width="26" height="7" fill="#cf3a3a"/><rect x="56" y="32" width="26" height="7" fill="#f2c14b"/><rect x="82" y="32" width="26" height="7" fill="#7dc36b"/><rect x="108" y="32" width="26" height="7" fill="#f2c14b"/><rect x="134" y="32" width="26" height="7" fill="#7dc36b"/>
            <rect x="30" y="40" width="26" height="7" fill="#7dc36b"/><rect x="56" y="40" width="26" height="7" fill="#cf3a3a"/><rect x="82" y="40" width="26" height="7" fill="#f2c14b"/><rect x="108" y="40" width="26" height="7" fill="#7dc36b"/><rect x="134" y="40" width="26" height="7" fill="#f2c14b"/>
          </g>
          <g fill="#8a95a0"><rect x="3" y="10" width="22" height="2"/><rect x="3" y="18" width="22" height="2"/><rect x="3" y="26" width="22" height="2"/><rect x="3" y="34" width="22" height="2"/><rect x="3" y="42" width="22" height="2"/></g>
        </svg>
        <p class="back-caption">Constantly track the quality and performance of individual distribution outlets based on the underwriting score of each policy.</p>
      </div>
    </div>

    <p class="back-statement">Veltrisk detects, measures and presents actionable options to correct the insurance company effects of adverse selection within any P&amp;C portfolio.</p>

    <div class="section-bar" style="top:175px;"><span style="left:40px;">UNDERWRITING SCORE</span><span style="left:225px;">TREND AND LOSS RATIO</span></div>

    <div class="back-grid" style="top:193px;">
      <div>
        <svg width="160" height="78" viewBox="0 0 160 78" aria-label="Underwriting score bar chart">
          <rect x="40" y="2" width="5" height="4" fill="#5b7db8"/><rect x="90" y="2" width="5" height="4" fill="#7fbf7a"/>
          <g stroke="#d6dde3" stroke-width=".5"><line x1="14" y1="14" x2="156" y2="14"/><line x1="14" y1="30" x2="156" y2="30"/><line x1="14" y1="46" x2="156" y2="46"/><line x1="14" y1="62" x2="156" y2="62"/></g>
          <line x1="14" y1="70" x2="156" y2="70" stroke="#8a95a0" stroke-width=".6"/>
          <rect x="22" y="20" width="14" height="50" fill="#5b7db8"/><rect x="37" y="40" width="14" height="30" fill="#7fbf7a"/>
          <rect x="70" y="28" width="14" height="42" fill="#5b7db8"/><rect x="85" y="46" width="14" height="24" fill="#7fbf7a"/>
          <rect x="118" y="36" width="14" height="34" fill="#5b7db8"/><rect x="133" y="50" width="14" height="20" fill="#7fbf7a"/>
        </svg>
        <p class="back-caption">Discover the pricing imbalances within the portfolio. These imbalances are the main driver of the adverse selection.</p>
      </div>
      <div>
        <svg width="160" height="78" viewBox="0 0 160 78" aria-label="Trend and loss ratio bubble chart">
          <line x1="16" y1="4" x2="16" y2="70" stroke="#8a95a0" stroke-width=".6"/>
          <line x1="16" y1="70" x2="156" y2="70" stroke="#8a95a0" stroke-width=".6"/>
          <g stroke="#d6dde3" stroke-width=".5"><line x1="16" y1="20" x2="156" y2="20"/><line x1="16" y1="36" x2="156" y2="36"/><line x1="16" y1="52" x2="156" y2="52"/></g>
          <line x1="30" y1="60" x2="130" y2="12" stroke="#8fb0c8" stroke-width=".6"/>
          <g fill="#3a97c7" stroke="#1f6f9c" stroke-width=".5">
            <circle cx="48" cy="52" r="7"/><circle cx="56" cy="42" r="6"/><circle cx="62" cy="30" r="7"/><circle cx="122" cy="16" r="8"/>
          </g>
        </svg>
        <p class="back-caption">Show trends within the portfolio in real time covering premium adequacy and the quality of all business being written.</p>
      </div>
    </div>

    <div class="section-bar" style="top:300px;"><span style="left:40px;">PORTFOLIO EXPOSURE</span><span style="left:225px;">PREMIUM CHANGE</span></div>
    <p class="back-note">Report on detailed analyses including sales trend and profitability trends. This allows for a method of managing distribution channels while addressing pricing imbalances.</p>

    <div class="back-grid" style="top:344px;">
      <svg width="160" height="80" viewBox="0 0 160 80" aria-label="Portfolio exposure line chart">
        <line x1="16" y1="4" x2="16" y2="64" stroke="#8a95a0" stroke-width=".6"/>
        <line x1="16" y1="64" x2="156" y2="64" stroke="#8a95a0" stroke-width=".6"/>
        <g stroke="#d6dde3" stroke-width=".5"><line x1="16" y1="16" x2="156" y2="16"/><line x1="16" y1="28" x2="156" y2="28"/><line x1="16" y1="40" x2="156" y2="40"/><line x1="16" y1="52" x2="156" y2="52"/></g>
        <polyline points="18,20 26,24 34,22 42,28 50,26 58,30 66,27 74,31 82,29 90,33 98,30 106,34 114,32 122,38 130,40 138,46 146,42 154,48" fill="none" stroke="#4fb08c" stroke-width="1.2"/>
        <g fill="#8a95a0"><rect x="18" y="68" width="3" height="9"/><rect x="30" y="68" width="3" height="9"/><rect x="42" y="68" width="3" height="9"/><rect x="54" y="68" width="3" height="9"/><rect x="66" y="68" width="3" height="9"/><rect x="78" y="68" width="3" height="9"/><rect x="90" y="68" width="3" height="9"/><rect x="102" y="68" width="3" height="9"/><rect x="114" y="68" width="3" height="9"/><rect x="126" y="68" width="3" height="9"/><rect x="138" y="68" width="3" height="9"/><rect x="150" y="68" width="3" height="9"/></g>
      </svg>
      <svg width="160" height="80" viewBox="0 0 160 80" aria-label="Premium change bar chart">
        <rect x="40" y="2" width="5" height="4" fill="#5b7db8"/><rect x="90" y="2" width="5" height="4" fill="#7fbf7a"/>
        <line x1="14" y1="70" x2="156" y2="70" stroke="#8a95a0" stroke-width=".6"/>
        <rect x="22" y="14" width="14" height="56" fill="#5b7db8"/><rect x="37" y="44" width="14" height="26" fill="#7fbf7a"/>
        <rect x="70" y="24" width="14" height="46" fill="#5b7db8"/><rect x="85" y="48" width="14" height="22" fill="#7fbf7a"/>
        <rect x="118" y="32" width="14" height="38" fill="#5b7db8"/><rect x="133" y="52" width="14" height="18" fill="#7fbf7a"/>
      </svg>
    </div>

    <footer class="back-footer">
      <p class="footer-about">Brightfen Metrics provides breakthrough portfolio analytics powered by machine learning and modern statistical techniques, enabling property and casualty insurers to achieve superior performance.</p>
      <div class="footer-brand"><i></i>Brightfen Metrics</div>
      <p class="footer-contact">Brightfen Metrics, 415 Harlow Street<br>Suite 220, Orlenport, QX 00471<br>Phone: 555.010.0148 • Fax: 555.010.0149<br><strong>www.brightfenmetrics.example</strong></p>
    </footer>
  </section>

</body>
</html>
```